Football and Sports Management Agency Stationary

We have a logo, fonts, website and colour palette.
We need the logo refined by a proper designer and then business stationary designed. You can see on the website how it needs adjusting by a designers eye.
The company is a high end sports management company aiming to attract and represent professional athletes. The name Velorin is to indicate a 'Constellation of Stars' ie our clients. The dots on the star should be slightly different sizes to reflect that some clients will be bigger than others.
Colours:
#e6e6e6
#edd2a4
#caaa72 (main gold and also used on site)
#3f3f42
#001d38
#edeced (on website)
#191c23 (on website)
Font:
QT (velorin)
QT Melbrook (sports management)
We would like:
- Letterhead (word and indesign and PDF print format). I have attached an example for one I like. It's quiet a clean design with the contact details and address taking up only a small amount of room.
- Business card (dark on the back with the logo, personal details on the front). Only needs name, title, email, website and phone number. No company address (in PDF and indesign format)
- Powerpoint slide theme
- Logo in vector format for light and dark versions and single colour versions. And optimised web version
- Simple brand guide PDF showing colour, font and logo (a one/two page PDF)
Any questions, please ask.
NEW INFO:
Contact Details
Maren Solwick
Director
Mobile: +44 7630 218 977
Phone: +44 0113 872 604
Email: maren@velorinathletic.example
Web: velorinathletic.example
Corran Lodge, 14 Mill Bank Road, Stockport, SK4 9TW
Company number 40718362
Target Market(s)
Professional athletes, professional sports teams.
Industry/Entity Type
Management
Requirements
Must have
- NEW
- The designs must look cool, classy and high quality. My suggestion for this is to keep the text small and precise with uncomplicated design.
Nice to have
- Application of brand displayed on stationary and additional pieces of stationary branded.
- Draw some inspiration from the website. eg the slant angles used separate the sections.
Should not have
- Don't create new logos etc.

```html
<!DOCTYPE html>
<html lang="en">
<head>
<meta charset="utf-8">
<title>Velorin Stationery Suite</title>
<link href="https://fonts.googleapis.com/css2?family=Montserrat:wght@300;400&family=Open+Sans:wght@400;600&display=swap" rel="stylesheet">
<style>
:root{
  --bg:#ececec;
  --paper:#f4f4f3;
  --slide:#e9e9e9;
  --dark:#3f3f42;
  --gold:#caaa72;
  --gold-soft:#bd9d69;
  --ink:#4a4a4d;
  --muted:#7d7d80;
}
*{margin:0;padding:0;box-sizing:border-box}
html,body{width:1028px;height:1200px;overflow:hidden;background:var(--bg)}
body{position:relative;font-family:"Open Sans",Arial,sans-serif;color:var(--ink)}
.piece{position:absolute;overflow:hidden}
.wordmark{font-family:"Montserrat",Arial,sans-serif;font-weight:300;letter-spacing:.42em;color:var(--ink);white-space:nowrap}
.band{position:absolute;left:0;bottom:0;width:100%}
.tiny{font-size:4px;line-height:1.45;color:var(--muted)}

/* letterhead */
.letterhead{left:217px;top:94px;width:280px;height:396px;background:var(--paper)}
.letterhead .wordmark{position:absolute;left:30px;top:28px;font-size:10px}
.letterhead .address{position:absolute;left:132px;top:22px;width:66px;text-align:right}
.letterhead .contact{position:absolute;left:204px;top:22px;border-left:.5px solid #bbb;padding-left:4px}

/* presentation folder */
.folder{left:544px;top:76px;width:331px;height:418px;background:var(--dark)}
.folder .wordmark{position:absolute;right:28px;top:98px;font-size:21px;color:#f2f2f2}
.folder .web{position:absolute;left:38px;top:374px;font-size:9px;color:var(--dark);font-family:"Open Sans",Arial,sans-serif}

/* business cards */
.card-front{left:116px;top:526px;width:126px;height:71px;background:var(--paper)}
.card-front .wordmark{position:absolute;left:42px;top:14px;font-size:8px}
.card-front .person{position:absolute;left:20px;top:49px;font-size:4px;color:var(--gold);line-height:1.3}
.card-front .person b{font-weight:400;display:block}
.card-front .person span{color:#ddd}
.card-front .lines{position:absolute;left:62px;top:47px;border-left:.5px solid #888;padding-left:3px;color:#ddd;font-size:3px;line-height:1.45}
.card-back{left:116px;top:618px;width:126px;height:71px;background:var(--dark)}
.card-back .wordmark{position:absolute;left:46px;top:30px;font-size:8px;color:#e6e6e6}

/* envelopes */
.env-front{left:275px;top:536px;width:313px;height:150px;background:var(--paper)}
.env-front .wordmark{position:absolute;left:22px;top:36px;font-size:9px}
.env-front .return{position:absolute;left:22px;top:55px;width:70px}
.env-back{left:618px;top:536px;width:314px;height:150px;background:var(--paper)}
.env-back .seal{position:absolute;left:153px;top:21px;width:8px;height:8px;border-radius:50%;background:#f1e6d2}

/* slides */
.slide{width:257px;height:193px;background:var(--slide)}
.slide .title{position:absolute;left:14px;top:14px;font-size:10.5px;font-weight:600;color:var(--gold)}
.slide .sub{position:absolute;left:14px;top:28px;font-size:5.5px;font-weight:600;color:var(--ink)}
.slide .rule{position:absolute;left:55px;right:14px;top:31px;border-top:.6px solid #9a9a9a}
.s1{left:102px;top:733px}
.s2{left:383px;top:733px}
.s3{left:670px;top:733px}
.s4{left:102px;top:938px}
.s5{left:383px;top:938px}
.s6{left:670px;top:938px;background:var(--dark)}

.s1 .wordmark{position:absolute;left:85px;top:45px;font-size:17px;letter-spacing:.5em}
.s1 .welcome{position:absolute;left:0;width:100%;top:132px;text-align:center;color:var(--gold);font-size:12px;line-height:1.25;font-family:"Open Sans",Arial,sans-serif}
.s1 .welcome small{font-size:10px;display:block}

.photos{position:absolute;left:19px;top:54px;display:flex;gap:7px}
.photo{width:50px;height:50px;background:var(--dark);border:1px solid #cfcfcf;color:#ddd;font-size:6px;display:flex;align-items:center;justify-content:center}
.team{position:absolute;left:19px;top:116px;display:flex;gap:7px}
.member{width:51px}
.member h4{font-size:5px;font-weight:400;color:var(--gold)}
.member em{font-size:4.5px;display:block;margin:1px 0 6px}
.member p,.group p,.txt{font-size:3.6px;line-height:1.45;color:var(--ink);text-align:justify}

.groups{position:absolute;left:15px;top:48px;width:232px;display:grid;grid-template-columns:1fr 1fr;column-gap:10px;row-gap:16px}
.group h4{font-size:5.5px;font-weight:400;color:var(--gold);margin-bottom:3px}

.chart{position:absolute;left:24px;top:48px}
.s4 .side{position:absolute;left:155px;top:48px;width:72px;text-align:left}
.s4 .foot{position:absolute;left:20px;top:142px;width:218px}
.s5 .para{position:absolute;left:20px;top:62px;width:112px;text-align:center}
.s5 .para2{position:absolute;left:20px;top:138px;width:112px;text-align:center}
.pie{position:absolute;left:156px;top:56px}
.legend{position:absolute;left:158px;top:124px;font-size:3.6px}
.legend div{display:flex;align-items:center;gap:3px;margin-bottom:3px;padding-bottom:2px;border-bottom:.5px solid #bbb;width:70px}
.legend i{width:5px;height:5px;display:inline-block}
.s5 .note{position:absolute;left:158px;top:148px;width:72px}

.s6 .thanks{position:absolute;left:0;width:100%;top:62px;text-align:center;color:var(--gold);font-family:"Montserrat",Arial,sans-serif;font-weight:300;font-size:36px;line-height:.95}
.s6 .thanks span{display:block;font-size:20px}
.s6 .info{position:absolute;left:0;width:100%;top:165px;text-align:center;font-size:4px;line-height:1.4;color:#ddd}
.s6 .info b{color:var(--gold);font-weight:400}
</style>
</head>
<body>

<!-- Letterhead -->
<section class="piece letterhead">
  <div class="wordmark">VELORIN</div>
  <div class="address tiny">Corran Lodge<br>14 Mill Bank Road<br>Stockport, SK4 9TW<br>Company number 40718362</div>
  <div class="contact tiny">+44 0113 872 604<br>+44 7630 218 977<br>maren@velorinathletic.example<br>velorinathletic.example</div>
  <svg class="band" width="280" height="30" viewBox="0 0 280 30">
    <polygon points="0,17 280,3 280,30 0,30" fill="var(--dark)"/>
    <polygon points="0,14 280,0 280,3 0,17" fill="var(--gold)"/>
  </svg>
</section>

<!-- Presentation folder -->
<section class="piece folder">
  <svg width="331" height="418" viewBox="0 0 331 418" style="position:absolute;left:0;top:0">
    <polygon points="0,0 331,418 0,418" fill="var(--gold-soft)"/>
    <rect x="0" y="0" width="14" height="418" fill="var(--gold-soft)"/>
    <line x1="8" y1="0" x2="8" y2="418" stroke="#a98b5b" stroke-width=".6"/>
  </svg>
  <div class="wordmark">VELORIN</div>
  <div class="web">www.velorinathletic.example</div>
</section>

<!-- Business card, front -->
<section class="piece card-front">
  <div class="wordmark">VELORIN</div>
  <svg class="band" width="126" height="37" viewBox="0 0 126 37">
    <polygon points="0,11 126,2 126,37 0,37" fill="var(--dark)"/>
    <polygon points="0,10 126,1 126,2 0,11" fill="var(--gold)"/>
  </svg>
  <div class="person"><b>MAREN SOLWICK</b><span>DIRECTOR</span></div>
  <div class="lines">+44 0113 872 604<br>+44 7630 218 977<br>maren@velorinathletic.example<br>velorinathletic.example</div>
</section>

<!-- Business card, back -->
<section class="piece card-back">
  <div class="wordmark">VELORIN</div>
</section>

<!-- DL envelope, front -->
<section class="piece env-front">
  <div class="wordmark">VELORIN</div>
  <div class="return tiny">Corran Lodge, 14 Mill Bank Road, Stockport, SK4 9TW</div>
  <svg class="band" width="313" height="8" viewBox="0 0 313 8">
    <polygon points="0,4 313,2 313,8 0,8" fill="var(--dark)"/>
    <polygon points="0,3 313,0 313,2 0,4" fill="var(--gold)"/>
  </svg>
</section>

<!-- DL envelope, back -->
<section class="piece env-back">
  <svg width="314" height="56" viewBox="0 0 314 56" style="position:absolute;left:0;top:0">
    <polygon points="0,0 314,0 308,53 6,53" fill="var(--gold-soft)"/>
  </svg>
  <div class="seal"></div>
</section>

<!-- Slide: title -->
<section class="piece slide s1">
  <div class="wordmark">VELORIN</div>
  <svg class="band" width="257" height="93" viewBox="0 0 257 93">
    <polygon points="0,18 257,0 257,93 0,93" fill="var(--dark)"/>
    <polygon points="0,15 257,-3 257,0 0,18" fill="var(--gold)"/>
  </svg>
  <div class="welcome">WELCOME TO OUR<br>PRESENTATION NAME<small>DESCRIPTION</small></div>
</section>

<!-- Slide: team -->
<section class="piece slide s2">
  <div class="title">Heading Here</div>
  <div class="sub">Sub Heading</div>
  <div class="rule"></div>
  <div class="photos">
    <div class="photo">Photo</div><div class="photo">Photo</div><div class="photo">Photo</div><div class="photo">Photo</div>
  </div>
  <div class="team">
    <div class="member"><h4>Team member1</h4><em>Title</em><p>Short profile of the athlete and their role here.</p></div>
    <div class="member"><h4>Team member2</h4><em>Title</em><p>Short profile of the athlete and their role here.</p></div>
    <div class="member"><h4>Team member3</h4><em>Title</em><p>Short profile of the athlete and their role here.</p></div>
    <div class="member"><h4>Team member4</h4><em>Title</em><p>Short profile of the athlete and their role here.</p></div>
  </div>
</section>

<!-- Slide: groups -->
<section class="piece slide s3">
  <div class="title">Heading Here</div>
  <div class="sub">Sub Heading</div>
  <div class="rule"></div>
  <div class="groups">
    <div class="group"><h4>Group1</h4><p>Brief outline of this group, its members and the goals set for the season ahead.</p></div>
    <div class="group"><h4>Group4</h4><p>Brief outline of this group, its members and the goals set for the season ahead.</p></div>
    <div class="group"><h4>Group2</h4><p>Brief outline of this group, its members and the goals set for the season ahead.</p></div>
    <div class="group"><h4>Group5</h4><p>Brief outline of this group, its members and the goals set for the season ahead.</p></div>
    <div class="group"><h4>Group3</h4><p>Brief outline of this group, its members and the goals set for the season ahead.</p></div>
    <div class="group"><h4>Group6</h4><p>Brief outline of this group, its members and the goals set for the season ahead.</p></div>
  </div>
</section>

<!-- Slide: bar chart -->
<section class="piece slide s4">
  <div class="title">Heading Here</div>
  <div class="sub">Sub Heading</div>
  <div class="rule"></div>
  <svg class="chart" width="110" height="84" viewBox="0 0 110 84">
    <g stroke="#cfcfcf" stroke-width=".6">
      <line x1="0" y1="4" x2="104" y2="4"/><line x1="0" y1="14" x2="104" y2="14"/>
      <line x1="0" y1="24" x2="104" y2="24"/><line x1="0" y1="34" x2="104" y2="34"/>
      <line x1="0" y1="44" x2="104" y2="44"/><line x1="0" y1="54" x2="104" y2="54"/>
      <line x1="0" y1="64" x2="104" y2="64"/><line x1="0" y1="74" x2="104" y2="74"/>
    </g>
    <rect x="24" y="4" width="12" height="76" fill="var(--gold-soft)"/>
    <rect x="41" y="13" width="12" height="67" fill="var(--gold-soft)"/>
    <rect x="58" y="30" width="12" height="50" fill="var(--gold-soft)"/>
    <rect x="75" y="19" width="12" height="61" fill="var(--gold-soft)"/>
    <g fill="#f4ead8" font-size="3.5" font-family="Open Sans, Arial, sans-serif">
      <text transform="translate(32,78) rotate(-90)">Year 1</text>
      <text transform="translate(49,78) rotate(-90)">Year 2</text>
      <text transform="translate(66,78) rotate(-90)">Year 3</text>
      <text transform="translate(83,78) rotate(-90)">Year 4</text>
    </g>
  </svg>
  <p class="side txt">Growth in client value across four seasons, shown by quarter for each division of the agency.</p>
  <p class="foot txt">Each bar reflects total contract value under management, measured at the close of the period and compared with the previous year.</p>
</section>

<!-- Slide: pie chart -->
<section class="piece slide s5">
  <div class="title">Heading Here</div>
  <div class="sub">Sub Heading</div>
  <div class="rule"></div>
  <p class="para txt" style="text-align:center">Share of revenue by sport across the current portfolio. Football remains the largest part, followed by rugby, cricket and athletics, with steady growth in every area over the last year of representation.</p>
  <p class="para2 txt" style="text-align:center">Figures are rounded and based on signed agreements only.</p>
  <svg class="pie" width="60" height="60" viewBox="-30 -30 60 60">
    <circle r="28" fill="var(--gold-soft)"/>
    <path d="M0,0 L4.86,-27.57 A28,28 0 0 1 27.89,2.44 Z" fill="var(--dark)" stroke="var(--slide)" stroke-width="1"/>
    <path d="M0,0 L27.89,2.44 A28,28 0 0 1 25.38,11.83 Z" fill="var(--gold-soft)" stroke="var(--slide)" stroke-width="1"/>
    <path d="M0,0 L25.38,11.83 A28,28 0 0 1 -4.86,27.57 Z" fill="var(--dark)" stroke="var(--slide)" stroke-width="1"/>
  </svg>
  <div class="legend">
    <div><i style="background:var(--gold-soft)"></i>Football share 50%</div>
    <div><i style="background:var(--dark)"></i>Other sports 50%</div>
  </div>
  <p class="note txt">Updated at the end of each quarter.</p>
</section>

<!-- Slide: closing -->
<section class="piece slide s6">
  <div class="thanks">Thanks<span>For Coming</span></div>
  <div class="info">Corran Lodge, 14 Mill Bank Road, Stockport, SK4 9TW<br><b>P:</b> +44 0113 872 604 <b>M:</b> +44 7630 218 977 <b>E:</b> maren@velorinathletic.example<br><b>W:</b> velorinathletic.example | Company number 40718362</div>
</section>

</body>
</html>
```